TalkBridge - Language Coaching Services

Sleek, innovative, trendy design for Language Coaching business.

TalkBridge is a new UK based company that provides Language Coaching services. We offer highly personalized on-line and face to face language courses. We also impart learning techniques workshops based on the latest neuroscience research for second-language acquisition.

Target Market(s)

Industry/Entity Type

Consulting

Contact Information for Business Card

TalkBridge
ElenaVT@talkbridge-demo.co.uk
TalkBridge-demo.co.uk
Leeds, UK

Font styles to use
Sans Serif

```html
<!DOCTYPE html>
<html lang="en">
<head>
<meta charset="utf-8">
<title>TalkBridge – Business Card</title>
<link href="https://fonts.googleapis.com/css2?family=Roboto:wght@400;500;700&display=swap" rel="stylesheet">
<style>
  :root {
    --stage: #26282c;
    --card: #0d0e10;
    --blue: #1fa3e0;
    --blue-deep: #0f7fc0;
    --white: #f2f4f6;
  }
  * { margin: 0; padding: 0; box-sizing: border-box; }
  html, body {
    width: 1200px; height: 900px; overflow: hidden;
    background: var(--stage);
    font-family: "Roboto", Arial, sans-serif;
  }
  .stage {
    position: relative; width: 1200px; height: 900px;
    display: flex; flex-direction: column; align-items: center; justify-content: center; gap: 60px;
  }
  .card {
    position: relative; width: 620px; height: 350px;
    background: var(--card);
    border-radius: 26px;
    overflow: hidden;
    box-shadow: 0 18px 40px rgba(0,0,0,.45);
  }

  /* Front side */
  .card-front .accent-band {
    position: absolute; left: 0; top: 0; bottom: 0; width: 22px;
    background: linear-gradient(180deg, var(--blue), var(--blue-deep));
  }
  .card-front .details {
    position: absolute; right: 48px; top: 46px;
    text-align: right; color: var(--white);
  }
  .person-name {
    color: var(--blue); font-weight: 700; font-size: 30px; letter-spacing: .5px;
  }
  .person-role { font-weight: 500; font-size: 20px; margin-top: 2px; }
  .divider {
    display: block; width: 24px; height: 4px; background: var(--blue);
    margin: 22px 0 22px auto;
  }
  .contact-list { list-style: none; }
  .contact-list li {
    display: flex; align-items: center; justify-content: flex-end; gap: 12px;
    font-size: 19px; font-weight: 500; line-height: 1.55;
  }
  .contact-list svg { width: 18px; height: 18px; fill: var(--blue); flex: none; }

  /* Back side */
  .card-back .brand {
    position: absolute; inset: 0 0 14px 0;
    display: flex; align-items: center; justify-content: center; gap: 22px;
  }
  .brand-mark {
    width: 96px; height: 96px; border-radius: 50%;
    border: 7px solid var(--blue);
  }
  .brand-name {
    color: var(--blue); font-weight: 700; font-size: 52px; letter-spacing: 2px;
  }
  .card-back .edge-band {
    position: absolute; left: 0; right: 0; bottom: 0; height: 14px;
    background: var(--blue);
  }
</style>
</head>
<body>
<main class="stage">

  <section class="card card-front" aria-label="Business card front">
    <div class="accent-band"></div>
    <div class="details">
      <h1 class="person-name">JOHNATHAN DOE</h1>
      <p class="person-role">Manager</p>
      <span class="divider"></span>
      <ul class="contact-list">
        <li>020 7946 0418
          <svg viewBox="0 0 24 24" aria-hidden="true"><path d="M6.6 10.8a15.1 15.1 0 0 0 6.6 6.6l2.2-2.2a1 1 0 0 1 1-.25 11.4 11.4 0 0 0 3.6.57 1 1 0 0 1 1 1V20a1 1 0 0 1-1 1A17 17 0 0 1 3 4a1 1 0 0 1 1-1h3.5a1 1 0 0 1 1 1c0 1.25.2 2.45.57 3.57a1 1 0 0 1-.25 1z"/></svg>
        </li>
        <li>ElenaVT@talkbridge-demo.co.uk
          <svg viewBox="0 0 24 24" aria-hidden="true"><path d="M3 5h18a1 1 0 0 1 1 1v12a1 1 0 0 1-1 1H3a1 1 0 0 1-1-1V6a1 1 0 0 1 1-1zm9 7.5L4 7.5V9l8 5 8-5V7.5z"/></svg>
        </li>
        <li>Leeds, UK
          <svg viewBox="0 0 24 24" aria-hidden="true"><path d="M12 2a7 7 0 0 1 7 7c0 5-7 13-7 13S5 14 5 9a7 7 0 0 1 7-7zm0 4.5A2.5 2.5 0 1 0 12 11.5 2.5 2.5 0 0 0 12 6.5z"/></svg>
        </li>
        <li>TalkBridge-demo.co.uk
          <svg viewBox="0 0 24 24" aria-hidden="true"><path d="M12 2a10 10 0 1 0 0 20 10 10 0 0 0 0-20zm-1 2.1V8H7.3A8 8 0 0 1 11 4.1zm2 0A8 8 0 0 1 16.7 8H13zM6.3 10H11v4H6.3a8 8 0 0 1 0-4zm6.7 0h4.7a8 8 0 0 1 0 4H13zm-5.7 6H11v3.9A8 8 0 0 1 7.3 16zm5.7 0h3.7A8 8 0 0 1 13 19.9z"/></svg>
        </li>
      </ul>
    </div>
  </section>

  <section class="card card-back" aria-label="Business card back">
    <div class="brand">
      <span class="brand-mark"></span>
      <span class="brand-name">TALKBRIDGE</span>
    </div>
    <div class="edge-band"></div>
  </section>

</main>
</body>
</html>
```